Cover Design

Need a book cover design for a book based on inspirational stories of people with disability. The book title is 'Where the River Bends'. It contains 15 real life stories of people with different kinds of disabilities, people who have risen above their handicaps to achieve extra-ordinary milestones in their lives. Need a highly positive cover showcasing hope,optimism, rising above one's limits, pushing boundaries

Some Guidelines: Front Cover Title:________________________________Where the River Bends Author Name: ________________________________Mirel Back Cover Blurb "Did you know that India’s youngest patent holder is a ten year old boy who is confined to a wheelchair and whose inventions of variants of chess for six, twelve and sixty players resulted out of his desire to play with his friends? Have you heard of the army major who was declared dead in the Venthar war but is today India’s first blade runner? Can a woman without hands be India’s leading painter? Or can a man bedridden for twenty years of his life be lightening thousands of other lives? What is the first thought that comes to your mind when you see a differently-abled person? Is it pity? Is it sympathy? The real-life stories of the people in this book will make you think otherwise. Here are 15 differently-abled people who have fought against all odds to achieve their dreams. The lives and achievements of these real life heroes are truly inspirational. This book is a tribute to their courage, passion and zest for life. They will challenge your notion of the impossible. They will inspire you to live life to the fullest." Bar code box in vector format Spine Final Spine Width (in mm): ___________________ It is 5.1 X 7.75 inches. Keep the spine flexible._____________ Any logo that needs to appear on the spine: Publisher's logo (Quellmoor Publishers) Target Audience: People in the age group 20-40 Content Synopsis( One paragraph) The book is about life stories of differently-abled people. 15 stories of these people include visually, hearing, locomotive, genetic disabilities. Stories are about how despite their disabilities, these people have made big in life and are an inspiration for many. These people have achieved a lot of success despite their body/mind being handicapped. What is the look and feel you want for the cover: (Kindly provide me three four adjectives): Courage, Positive, Breaking societal myths, Life

Reason: I am out of town for the next 2 days.

Reason: Need more designs for evaluation.

Some images which I quite liked and can be used as pointers: http://www.pictofind.example/view?src=http%3A%2F%2Fimg.stockvaro.example%2Fpreview%2F553812%2F904417263%2Foptimism-word-cloud-thumb-up-904417263.jpg&ref=http%3A%2F%2Fwww.stockvaro.example%2Fimage-904417263%2Foptimism-word-cloud-thumb-up.html&h=470&w=384&page=4 http://www.brightmeadow.example/quotes/Quote-Life-is-a-Gift-Orlena-Vask.jpg http://pennoriel.files.blogvessel.example/2011/04/life_beautiful8.jpg http://steadyharvest.example/wp-content/uploads/2011/09/Live-Life-200x300.jpg http://lanternsofthemorningdotnet.files.blogvessel.example/2013/01/life.jpg?w=608&h=400&crop=1 Would like to see designs around these concepts

Hi All I only use my first name. So, please drop off "Tolvane" from the cover.

Hi All Please place a placeholder on front/back cover for a quote from the book. Quote not final yet

Reason: One of the designer working on the cover is busy

The title has a smiley (happy face) in the end. Please incorporate that. "Where the River Bends :) "

Colors

Designer to choose colors to be used in the design.

Requirements
Must have
• The logo needs to appear on both the front cover and spine. I have attached the high resolution image of the logo in pdf .

```html
<!DOCTYPE html>
<html lang="en">
<head>
<meta charset="utf-8">
<title>Where the River Bends — Cover</title>
<link rel="stylesheet" href="https://fonts.googleapis.com/css2?family=Playfair+Display:ital,wght@0,400;1,400&family=Libre+Baskerville:ital@1&family=Open+Sans:wght@400;600;700&display=swap">
<style>
  :root {
    --sky-top: #4f7fae;
    --sky-mid: #a9bcc9;
    --glow: #fff3cf;
    --amber: #f1c27a;
    --wheat: #d79a3a;
    --wheat-deep: #9a5e1c;
    --spine: #4a5078;
    --ink: #111111;
    --paper: #ffffff;
    --smile: #f7c81b;
  }
  * { margin: 0; padding: 0; box-sizing: border-box; }
  html, body { width: 1200px; height: 867px; overflow: hidden; background: #ffffff; }
  .cover {
    position: relative;
    width: 1200px;
    height: 867px;
    overflow: hidden;
  }
  .scenery {
    position: absolute;
    inset: 0;
    background:
      radial-gradient(ellipse 380px 300px at 830px 500px, rgba(255,248,225,0.95), rgba(255,240,200,0) 70%),
      radial-gradient(ellipse 420px 260px at 160px 420px, rgba(255,240,205,0.8), rgba(255,240,205,0) 70%),
      linear-gradient(180deg, var(--sky-top) 0%, var(--sky-mid) 22%, var(--glow) 48%, var(--amber) 62%, var(--wheat) 75%, var(--wheat-deep) 100%);
  }
  .blurb {
    position: absolute;
    left: 21px;
    top: 192px;
    width: 522px;
    font-family: "Open Sans", sans-serif;
    font-weight: 600;
    font-size: 15.4px;
    line-height: 21.7px;
    color: var(--ink);
    text-align: justify;
  }
  .blurb p + p { margin-top: 21.7px; }

  .spine {
    position: absolute;
    left: 571px;
    top: 0;
    width: 58px;
    height: 867px;
    background: var(--spine);
    color: var(--paper);
  }
  .spine-title {
    position: absolute;
    top: 30px;
    left: 50%;
    transform: translateX(-50%);
    writing-mode: vertical-rl;
    font-family: "Playfair Display", serif;
    font-size: 34px;
    white-space: nowrap;
    display: flex;
    align-items: center;
  }
  .spine-title em { font-style: italic; margin-top: 8px; }
  .spine-title .smiley { width: 24px; height: 24px; margin-top: 10px; }
  .spine-author {
    position: absolute;
    top: 573px;
    left: 50%;
    transform: translateX(-50%);
    writing-mode: vertical-rl;
    font-family: "Open Sans", sans-serif;
    font-weight: 700;
    font-size: 24px;
    letter-spacing: 0.4em;
  }
  .spine-publisher {
    position: absolute;
    top: 750px;
    left: 50%;
    transform: translateX(-50%);
    writing-mode: vertical-rl;
    display: flex;
    align-items: center;
    font-family: "Open Sans", sans-serif;
    font-weight: 600;
    font-size: 12px;
    letter-spacing: 0.06em;
  }
  .spine-publisher .mark {
    width: 10px; height: 10px;
    background: var(--paper);
    margin-bottom: 6px;
  }

  .title {
    position: absolute;
    left: 0;
    top: 0;
    font-family: "Playfair Display", serif;
    font-weight: 400;
  }
  .title span { position: absolute; white-space: nowrap; line-height: 1; }
  .title-top { left: 768px; top: 40px; font-size: 76px; color: var(--paper); }
  .title-mid { left: 770px; top: 128px; font-size: 98px; color: var(--ink); }
  .title-key { left: 740px; top: 256px; font-size: 122px; font-style: italic; color: var(--paper); }
  .smiley {
    display: block;
    border-radius: 50%;
    background: radial-gradient(circle at 40% 35%, #ffe46b, var(--smile) 60%, #d99a00);
  }
  .title-smiley { position: absolute; left: 1064px; top: 290px; width: 82px; height: 82px; }

  .tagline {
    position: absolute;
    left: 658px;
    top: 653px;
    font-family: "Libre Baskerville", serif;
    font-style: italic;
    font-size: 16px;
    line-height: 21px;
    color: var(--ink);
  }
  .tagline span { display: block; }
  .tagline span:nth-child(2) { padding-left: 27px; }
  .tagline span:nth-child(3) { padding-left: 20px; }

  .author {
    position: absolute;
    left: 786px;
    top: 772px;
    font-family: "Open Sans", sans-serif;
    font-weight: 700;
    font-size: 46px;
    letter-spacing: 0.55em;
    color: var(--paper);
    line-height: 1;
  }
  .author-note {
    position: absolute;
    left: 733px;
    top: 828px;
    font-family: "Open Sans", sans-serif;
    font-size: 18.5px;
    color: var(--paper);
    white-space: nowrap;
  }
</style>
</head>
<body>
<main class="cover">
  <div class="scenery" role="img" aria-label="Photograph of a golden wheat field under a bright sunlit sky, with a person standing with arms raised on the front cover"></div>

  <section class="back-cover">
    <div class="blurb">
      <p>Did you know that India’s youngest patent holder is a ten year old boy who is confined to a wheelchair and whose inventions of variants of chess for six, twelve and sixty players resulted out of his desire to play with his friends? Have you heard of the army major who was declared dead in the Venthar war but is today India’s first blade runner? Can a woman without hands be India’s leading painter? Or can a man bedridden for twenty years of his life be lightening thousands of other lives?</p>
      <p>What is the first thought that comes to your mind when you see a differently-abled person? Is it pity? Is it sympathy? The real-life stories of the people in this book will make you think otherwise. Here are 15 differently-abled people who have fought against all odds to achieve their dreams. The lives and achievements of these real life heroes are truly inspirational. This book is a tribute to their courage, passion and zest for life. They will challenge your notion of the impossible. They will inspire you to live life to the fullest.</p>
    </div>
  </section>

  <aside class="spine">
    <div class="spine-title">Where the River <em>Bends</em><span class="smiley" role="img" aria-label="smiley icon"></span></div>
    <div class="spine-author">MIREL</div>
    <div class="spine-publisher"><span class="mark"></span>Quellmoor</div>
  </aside>

  <section class="front-cover">
    <h1 class="title">
      <span class="title-top">Where the</span>
      <span class="title-mid">River</span>
      <span class="title-key">Bends</span>
    </h1>
    <span class="smiley title-smiley" role="img" aria-label="smiley icon"></span>
    <p class="tagline"><span>"Stories of hope,</span><span>courage and</span><span>perseverance"</span></p>
    <p class="author">MIREL</p>
    <p class="author-note">the author of ‘Letters Beyond the Harbour’</p>
  </section>
</main>
</body>
</html>
```